Branding for Clearflow Honours program collateral

The Clearflow Honours, hosted by the Aqueduct Trade Union, are an annual awards program to recognise excellence in the Australian water industry. The awards presentation ceremony is held over a formal luncheon, with a MC and Keynote Speaker. The awards event is a premium experience for business professionals that work in the work sector. It is a corporate business luncheon with management level professionals in attendance. We are seeking branding design elements that we can use on all awards collateral including the website, printed invitation, event program, social media posts etc. The Clearflow Honours are well known in the industry and recognised by its logo and corporate colours (attached). We would like these incorporated into the design.

Target Market(s)

business professionals

Industry/Entity Type

Water Company

Requirements
Must have
• event logo, corporate colours

```html
<!DOCTYPE html>
<html lang="en">
<head>
<meta charset="utf-8">
<title>Clearflow Honours – South Australia</title>
<link rel="stylesheet" href="https://fonts.googleapis.com/css2?family=Montserrat:wght@400;500&display=swap">
<style>
  :root {
    --pink: #ff7dfb;
    --rose: #ffa3b4;
    --peach: #ffbb82;
    --white: #ffffff;
    --lime: #80ff00;
    --cyan: #00e4ff;
    --magenta: #f700f4;
    --orange: #ff8000;
  }
  * { margin: 0; padding: 0; box-sizing: border-box; }
  html, body { width: 1200px; height: 849px; overflow: hidden; }
  body { font-family: "Montserrat", sans-serif; color: var(--white); }

  .canvas {
    position: relative;
    width: 1200px;
    height: 849px;
    overflow: hidden;
    background: linear-gradient(90deg, var(--pink) 0%, var(--rose) 40%, var(--peach) 100%);
  }

  .title-frame {
    position: absolute;
    left: 58px;
    top: 111px;
    width: 670px;
    height: 114px;
  }
  .title-frame svg { position: absolute; inset: 0; overflow: visible; }

  .event-name {
    position: absolute;
    left: 58px;
    width: 670px;
    top: 128px;
    text-align: center;
    font-weight: 500;
    font-size: 60px;
    letter-spacing: 3px;
    line-height: 1;
  }
  .event-type {
    position: absolute;
    left: 58px;
    width: 670px;
    top: 213px;
    text-align: center;
    font-weight: 500;
    font-size: 20px;
    letter-spacing: 6px;
    line-height: 1;
  }
  .event-region {
    position: absolute;
    left: 58px;
    width: 670px;
    top: 260px;
    text-align: center;
    font-weight: 400;
    font-size: 17px;
    letter-spacing: 5px;
    line-height: 1;
  }

  .host {
    position: absolute;
    left: 84px;
    top: 600px;
    width: 220px;
    text-align: center;
  }
  .host-dot {
    display: block;
    width: 60px;
    height: 60px;
    margin: 18px auto 42px;
    border-radius: 50%;
    background: var(--white);
  }
  .host-name {
    font-weight: 500;
    font-size: 25px;
    line-height: 1.32;
  }

  .pattern-field {
    position: absolute;
    left: 552px;
    top: 0;
    width: 648px;
    height: 849px;
    clip-path: polygon(40% 0, 100% 0, 100% 100%, 30% 100%, 5% 60%, 0 40%);
    background:
      radial-gradient(circle at 70% 30%, rgba(128,255,0,0.75), transparent 45%),
      radial-gradient(circle at 85% 65%, rgba(0,228,255,0.7), transparent 40%),
      radial-gradient(circle at 50% 60%, rgba(247,0,244,0.55), transparent 35%),
      radial-gradient(circle at 90% 5%, rgba(255,128,0,0.7), transparent 30%),
      linear-gradient(180deg, rgba(128,255,0,0.35), rgba(0,228,255,0.35));
  }
</style>
</head>
<body>
  <main class="canvas">
    <div class="title-frame" aria-hidden="true">
      <svg width="670" height="114" viewBox="0 0 670 114">
        <polyline points="168,111 2.5,111 2.5,2.5 667.5,2.5 667.5,111 502,111"
                  fill="none" stroke="#ffffff" stroke-width="5"/>
      </svg>
    </div>
    <h1 class="event-name">Clearflow</h1>
    <p class="event-type">HONOURS</p>
    <p class="event-region">SOUTH AUSTRALIA</p>

    <div class="host">
      <span class="host-dot" aria-hidden="true"></span>
      <p class="host-name">Aqueduct Trade<br>Union</p>
    </div>

    <div class="pattern-field" role="img"
         aria-label="Cluster of isometric geometric blocks in lime, cyan, magenta and orange"></div>
  </main>
</body>
</html>
```